Buch-/E-Book-Cover im Bereich der Persönlichkeitsentwicklung
Zielgruppe
Wir arbeiten in der Persönlichkeitsentwicklung für Jugendliche. Dabei spezialisieren wir uns auf den Altersbereich 12 - 17 Jahre. Unser Ziel ist es jungen Menschen zu zeigen, wie Sie zu sich selbst finden und ein glückliches sowie erfolgreiches Leben führen können.
Aufgabenstellung
- Das Design sollte für die Eltern von Teenagern und auch für die Teenager selbst ausgelegt werden. Das Buch ist für die Jugendlichen (Mädchen und Jungen im Alter zwischen 12 Jahren und 17 Jahren) gedacht, wird allerdings meist von deren Mütter gekauft.
- Der Name des Autors lautet: Lukas Brenner
- Der Titel lautet: Junge Herzen finden Mut und Freude
- Der Untertitel lautet: Wie junge Leute ihren eigenen Weg erkennen
- Im Anhang befinden sich Designs, die ich gut finde (nur falls jemand weitere Ideen haben möchte)
- Format: 15,24 cm x 22,86 cm (6' x 9') [genaue Maße fürs Taschenbuch und Hardcover sind im Anhang (.zip Dateien)]
1. E-Book:
- Coverdateien sollten idealerweise 2 560 Pixel hoch und 1 600 Pixel breit sein. Zur Gewährleistung der bestmöglichen Qualität (insbesondere auf HD-Geräten) sollte das Bild mindestens 2 500 Pixel hoch sein.
- Format: TIFF (.tif/.tiff) oder JPEG (.jpeg/.jpg)
- DPI: 72 dpi
- Größe: Ihr Coverbild muss kleiner als 50 MB sein.
Hinweis: Vermeiden Sie es, Ihre Dateien zu komprimieren. Dies kann die Qualität Ihres Covers auf Lesegeräten beeinträchtigen. Das beste Ergebnis erzielen Sie mit Bildern, die eine Mindestauflösung von 300 ppi (Pixels per Inch) haben.
- Rahmen: Coverbilder mit weißem oder sehr hellem Hintergrund heben sich kaum vom weißen Hintergrund ab. Fügen Sie einen dünnen Rahmen (3–4 Pixel) in Mittelgrau hinzu, um die Ränder des Covers besser sichtbar zu machen.
2. + 3. Taschenbuch/Hardcover [genaue Maße fürs Taschenbuch und Hardcover sind im Anhang (.zip Dateien)] :
- Dateityp: Das Cover muss als einzelne PDF-Datei vorliegen und die hintere Coverseite, den Buchrücken und die vordere Coverseite als einzelnes Bild enthalten.
- Dateigröße: Coverdateien, die größer als 650 MB sind, können nicht konvertiert werden. Die Datei sollte maximal 40 MB groß sein, da sich bei großen Dateien der Druck verlangsamt.
- Die gen..

```html
<!DOCTYPE html>
<html lang="de">
<head>
<meta charset="utf-8">
<title>Junge Herzen finden Mut und Freude – Lukas Brenner</title>
<link href="https://fonts.googleapis.com/css2?family=Oswald:wght@600&family=Rubik+Dirt&family=Pompiere&display=swap" rel="stylesheet">
<style>
  :root {
    --page: #ffffff;
    --frame: #2a9aa6;
    --pink: #d90f6e;
    --pink-light: #e03a8e;
    --white: #ffffff;
    --ink: #2a0e1c;
  }
  html, body {
    margin: 0;
    padding: 0;
    width: 1200px;
    height: 1200px;
    overflow: hidden;
    background: var(--page);
  }
  .cover {
    position: absolute;
    left: 241px;
    top: 59px;
    width: 726px;
    height: 1087px;
    box-sizing: border-box;
    border: 1.5px solid var(--frame);
    background: linear-gradient(180deg, var(--pink) 0%, var(--pink) 55%, var(--pink-light) 100%);
    overflow: hidden;
  }
  .author {
    position: absolute;
    top: 34px;
    left: 0;
    width: 100%;
    text-align: center;
    font-family: "Oswald", sans-serif;
    font-weight: 600;
    font-size: 27px;
    letter-spacing: 1px;
    color: var(--white);
    text-transform: uppercase;
  }
  .title-big, .title-small {
    position: absolute;
    white-space: nowrap;
    line-height: 1;
  }
  .title-big {
    font-family: "Rubik Dirt", sans-serif;
    color: var(--white);
  }
  .title-small {
    font-family: "Pompiere", sans-serif;
    color: var(--ink);
    font-weight: 400;
  }
  .title-line1 { left: 36px; top: 168px; font-size: 90px; letter-spacing: -2px; transform: rotate(-4deg); }
  .title-connector1 { left: 246px; top: 268px; font-size: 66px; transform: rotate(-4deg); }
  .title-line2 { left: 62px; top: 330px; font-size: 150px; transform: rotate(-2deg); }
  .title-connector2 { left: 360px; top: 386px; font-size: 66px; }
  .title-line3 { right: 70px; top: 468px; font-size: 130px; transform: rotate(-2deg); }
  .subtitle {
    position: absolute;
    font-family: "Pompiere", sans-serif;
    font-size: 50px;
    color: var(--white);
    text-transform: uppercase;
    white-space: nowrap;
    line-height: 1;
  }
  .subtitle-1 { left: 112px; top: 652px; }
  .subtitle-2 { left: 178px; top: 708px; }
  .subtitle-3 { left: 250px; top: 764px; }
  .photo { position: absolute; }
  .photo-boy {
    left: 0;
    top: 735px;
    width: 272px;
    height: 352px;
    border-radius: 90px 110px 0 0;
    background: linear-gradient(180deg, #5a2c24 0%, #2a1a1a 35%, #141014 100%);
  }
  .photo-girl {
    left: 428px;
    top: 716px;
    width: 298px;
    height: 371px;
    border-radius: 110px 80px 0 0;
    background: linear-gradient(180deg, #5e3426 0%, #7a4a36 30%, #d8d6de 60%, #b9b8c8 100%);
  }
</style>
</head>
<body>
  <main class="cover">
    <div class="author">Lukas Brenner</div>

    <h1 aria-label="Junge Herzen finden Mut und Freude">
      <span class="title-big title-line1">Junge Herzen</span>
      <span class="title-small title-connector1">finden</span>
      <span class="title-big title-line2">Mut</span>
      <span class="title-small title-connector2">und</span>
      <span class="title-big title-line3">Freude</span>
    </h1>

    <div class="photo photo-boy" role="img" aria-label="Foto: Junge mit dunklem Shirt, Kopf gesenkt, Haare im Gesicht"></div>
    <div class="photo photo-girl" role="img" aria-label="Foto: Mädchen in gestreifter Bluse, wirbelt die langen Haare"></div>

    <p class="subtitle-wrap" aria-label="Wie junge Leute ihren eigenen Weg erkennen">
      <span class="subtitle subtitle-1">Wie junge Leute</span>
      <span class="subtitle subtitle-2">ihren eigenen Weg</span>
      <span class="subtitle subtitle-3">erkennen</span>
    </p>
  </main>
</body>
</html>
```